Calendar Ad / Flyer

Our law firm needs a calendar ad to place in a local calendar.
THE DEADLINE IS THIS THURSDAY 06/28/2018.

Attached is the ad used in last years calendar. A few notes on this...
**. This is by no means the model to follow.
Please be creative and do what makes more sense marketing wise.
1. Need to update the color scheme which corresponds to the new website at morvanlegal.net
2. The "MORVAN LEGAL | STANDING FIRM FOR YOUR FUTURE" should be put at the top and made larger
3. "KNOWN AND TRUSTED IN OUR COMMUNITY FOR OVER 21 YEARS" should be changed to "KNOWN AND TRUSTED IN OUR COMMUNITY FOR OVER 22 YEARS"
4. "Dorian K. Morvan, Esq." should be made larger and better positioned.
5. Under the list of practices, it should be changed to have:
"Personal Injury, Legal Malpractice, Unlicensed Contractors, Medical Malpractice, Civil Litigation"
6. Contact information (i.e. contact number, website, and address) should be better positioned
7. Placement of endorsement logos should stand out more.
8. New picture of head attorney is attached.

Last but not least... Give it your best shot!

```html
<!DOCTYPE html>
<html lang="en">
<head>
<meta charset="utf-8">
<title>Morvan Legal – Calendar Ad</title>
<link rel="stylesheet" href="https://fonts.googleapis.com/css2?family=Libre+Baskerville:ital,wght@0,400;0,700;1,400&family=Montserrat:wght@300;400;600&display=swap">
<style>
  :root {
    --gold: #c9a468;
    --ink: #232323;
    --ink-deep: #191919;
    --paper: #f1f1f1;
    --white: #ffffff;
    --muted: #6b6b6b;
    --serif: "Libre Baskerville", Georgia, serif;
    --sans: "Montserrat", Arial, sans-serif;
  }
  * { box-sizing: border-box; margin: 0; padding: 0; }
  html, body { width: 1200px; height: 858px; overflow: hidden; background: var(--paper); }
  .ad { position: relative; width: 1200px; height: 858px; font-family: var(--sans); }

  .info-panel {
    position: absolute; left: 0; top: 0; width: 635px; height: 758px;
    background: linear-gradient(160deg, #3a3a3a 0%, #2a2a2a 45%, #1f1f1f 100%);
  }
  .brand { position: absolute; left: 137px; top: 56px; display: flex; align-items: center; gap: 12px; }
  .brand-mark { width: 30px; height: 30px; background: var(--gold); }
  .brand-text { display: flex; flex-direction: column; }
  .brand-name { font-family: var(--sans); font-weight: 600; font-size: 26px; color: var(--gold); letter-spacing: 1px; line-height: 1; }
  .brand-tag { font-family: var(--sans); font-weight: 600; font-size: 8px; color: var(--gold); letter-spacing: 1.2px; margin-top: 5px; }

  .headline {
    position: absolute; left: 137px; top: 152px; width: 480px;
    font-family: var(--serif); font-weight: 700; font-size: 43px; line-height: 54px;
    color: var(--white); text-transform: uppercase;
  }
  .headline .accent { color: var(--gold); }

  .practice-list { position: absolute; left: 137px; top: 410px; list-style: none; }
  .practice-list li {
    display: flex; align-items: center; gap: 14px; height: 34px;
    font-weight: 600; font-size: 22px; color: var(--white);
  }
  .tick { width: 22px; height: 22px; flex: none; }

  .contact-band {
    position: absolute; left: 0; top: 600px; width: 635px; height: 158px;
    background: var(--ink-deep);
  }
  .call-label { position: absolute; left: 137px; top: 20px; font-family: var(--serif); font-weight: 700; font-size: 26px; color: var(--white); }
  .phone { position: absolute; left: 137px; top: 60px; display: flex; align-items: center; gap: 14px; }
  .phone-icon { width: 34px; height: 34px; background: var(--gold); display: flex; align-items: center; justify-content: center; }
  .phone-number { font-weight: 300; font-size: 38px; color: var(--white); letter-spacing: 0.5px; }
  .website { position: absolute; left: 137px; top: 114px; font-size: 20px; letter-spacing: 3px; color: var(--gold); text-transform: uppercase; }

  .attorney-photo {
    position: absolute; left: 635px; top: 0; width: 565px; height: 758px;
    background:
      radial-gradient(ellipse 40% 45% at 55% 55%, #8a8d92 0%, rgba(138,141,146,0) 100%),
      linear-gradient(100deg, #b89a86 0%, #d9c9b8 35%, #8b6a55 70%, #4a352b 100%);
  }
  .nameplate {
    position: absolute; left: 730px; top: 664px; width: 470px; height: 60px;
    background: rgba(25,25,25,0.92); border-radius: 12px 0 0 12px;
    display: flex; align-items: center; gap: 22px; padding-left: 30px;
  }
  .nameplate-role { font-size: 19px; letter-spacing: 3px; color: var(--white); }
  .nameplate-name { font-family: var(--serif); font-style: italic; font-size: 19px; color: var(--gold); }

  .footer-strip {
    position: absolute; left: 0; top: 758px; width: 1200px; height: 100px;
    background: linear-gradient(#f7f7f7, #e9e9e9);
  }
  .address { position: absolute; left: 137px; top: 30px; display: flex; align-items: center; gap: 14px; }
  .pin-icon { width: 34px; height: 34px; background: var(--gold); display: flex; align-items: center; justify-content: center; }
  .address-text { font-size: 14px; line-height: 19px; letter-spacing: 1px; color: var(--muted); text-transform: uppercase; }
  .endorsements { position: absolute; left: 740px; top: 25px; display: flex; gap: 34px; align-items: center; }
  .badge { width: 50px; height: 50px; }
  .badge-round { border-radius: 50%; background: #3e8fc6; }
  .badge-square { background: #1f5c8c; }
  .badge-bar { height: 30px; width: 54px; background: #c8282e; }
  .badge-seal { border-radius: 50%; background: #7a1f1f; }
</style>
</head>
<body>
<main class="ad">
  <section class="info-panel" role="img" aria-label="Dark city skyline background">
  </section>

  <div class="brand">
    <span class="brand-mark"></span>
    <div class="brand-text">
      <span class="brand-name">MORVAN LEGAL</span>
      <span class="brand-tag">STANDING FIRM FOR YOUR FUTURE</span>
    </div>
  </div>

  <h1 class="headline"><span class="accent">Known and<br>Trusted</span> in our<br>community for<br>over 22 years</h1>

  <ul class="practice-list">
    <li><svg class="tick" viewBox="0 0 22 22"><circle cx="11" cy="11" r="11" fill="#c9a468"/><path d="M6 11.5l3.3 3.3L16 8" fill="none" stroke="#232323" stroke-width="2.4"/></svg>Personal Injury</li>
    <li><svg class="tick" viewBox="0 0 22 22"><circle cx="11" cy="11" r="11" fill="#c9a468"/><path d="M6 11.5l3.3 3.3L16 8" fill="none" stroke="#232323" stroke-width="2.4"/></svg>Legal Malpractice</li>
    <li><svg class="tick" viewBox="0 0 22 22"><circle cx="11" cy="11" r="11" fill="#c9a468"/><path d="M6 11.5l3.3 3.3L16 8" fill="none" stroke="#232323" stroke-width="2.4"/></svg>Unlicensed Contractors</li>
    <li><svg class="tick" viewBox="0 0 22 22"><circle cx="11" cy="11" r="11" fill="#c9a468"/><path d="M6 11.5l3.3 3.3L16 8" fill="none" stroke="#232323" stroke-width="2.4"/></svg>Medical Malpractice</li>
    <li><svg class="tick" viewBox="0 0 22 22"><circle cx="11" cy="11" r="11" fill="#c9a468"/><path d="M6 11.5l3.3 3.3L16 8" fill="none" stroke="#232323" stroke-width="2.4"/></svg>Civil Litigation</li>
  </ul>

  <section class="contact-band">
    <p class="call-label">Call Today</p>
    <div class="phone">
      <span class="phone-icon"><svg width="20" height="20" viewBox="0 0 24 24"><path fill="#ffffff" d="M6.6 10.8a15.1 15.1 0 0 0 6.6 6.6l2.2-2.2c.3-.3.7-.4 1-.2 1.1.4 2.3.6 3.6.6.6 0 1 .4 1 1V20c0 .6-.4 1-1 1A17 17 0 0 1 3 4c0-.6.4-1 1-1h3.5c.6 0 1 .4 1 1 0 1.3.2 2.5.6 3.6.1.3 0 .7-.2 1z"/></svg></span>
      <span class="phone-number">(888)-555-0142</span>
    </div>
    <p class="website">morvanlegal.net</p>
  </section>

  <section class="attorney-photo" role="img" aria-label="Portrait of the head attorney in a grey suit and blue tie, standing in a warmly lit office"></section>

  <div class="nameplate">
    <span class="nameplate-role">ATTORNEY</span>
    <span class="nameplate-name">Dorian K. Morvan, Esq.</span>
  </div>

  <footer class="footer-strip">
    <div class="address">
      <span class="pin-icon"><svg width="18" height="20" viewBox="0 0 24 24"><path fill="#ffffff" d="M12 2a7 7 0 0 0-7 7c0 5.2 7 13 7 13s7-7.8 7-13a7 7 0 0 0-7-7zm0 9.5A2.5 2.5 0 1 1 12 6.5a2.5 2.5 0 0 1 0 5z"/></svg></span>
      <p class="address-text">1820 Harbor Crest Ave., Suite #305<br>Lakeview, CA 90410</p>
    </div>
    <div class="endorsements" aria-label="Endorsements">
      <span class="badge badge-round"></span>
      <span class="badge badge-square"></span>
      <span class="badge badge-bar"></span>
      <span class="badge badge-seal"></span>
    </div>
  </footer>
</main>
</body>
</html>
```